依頼詳細
<サイトマップ>
1 TOP
2 コンセプト
3 salon info
4 メニュー
5 当サロンのこだわり
6 サロンスケジュール
7 スタッフ(一覧)
8 スタッフ(詳細)
9 ヘアカタログ(一覧)
10 ヘアカタログ(詳細)
11 プロダクト(一覧)
12 プロダクト(詳細)
13 ブログ・ニュース(一覧)
14 ブログ・ニュース(詳細)
15 お客様の声(一覧)
16 お客様の声(詳細)
17 よくある質問
18 お問い合わせ
19 求人情報
20 クーポン

<デザインテイスト>
モダン / ナチュラル / 清潔な

<デザインカラー>
モノトーン調に差し色で茶系・緑系(サロン内の色合いと併せてリラックスできるようなソフトな色合い)

<サイトにおける要望>
1CMS導入による操作性向上
2デザイン性の向上

<顧客ターゲット>
・30~40代女性(主婦・子連れ)

【デザイン要望】
・手書き風のアイコンやイラストで遊び心があるデザインが希望です。
・サイトの上から下まで全体に繋がりがあるようなデザインが希望です。
・現在のサイト内にカレンダーが実装されていますが、
デザインとしてカレンダーを設ける場合は、googleカレンダーにしてください。
・予約が外部のためバナーなどを配置して頂けると嬉しいです。

【参考サイト】
◎GOOD
https://www.kavenda.jp/
手書き風のタッチと全体の抜け感のある雰囲気が良いです。
※こちらの参考サイトを元にデザインを提案いただきたいです。

◯OK
http://abc.brovantelo-press.jp
全体的にまとまってる感じが良いです。
https://qpl.renzokawabuchi.com
画面をスクロールした時のレイアウトの雰囲気が好きです。
https://www.pex.co.jp/recruit/
全体的にストーリー性のあり良いですが、使っている色が多いのがNGです。

✕NG
http://zolvane-inc.jp
カラフル✕動きの部分がサロンのイメージとは離れているので避けてほしいです。

【素材】
■サロン外観・内装写真(ロゴ無しです)
http://quillbox.jp/download/3a71c0d5e2f84b96a1d07c3e58f2b9a64e1d7c08
ダウンロードパスワード k4m52tzq
サイトURL
http://www.dolvik.com/
ページ数
1ページ
希望イメージ
シンプル 複雑
単色 カラフル
暗い 明るい
日常 高級
遊び心 厳粛
未来的 伝統的
女性的 男性的
希望する色
茶系、緑系、グレー系
納品ファイル
• イラストレーター形式 (.ai)
• フォトショップ形式 (.psd)
補足説明
■ピクセラン
素材として定期ダウンロードできる画像は使用して頂いて構いません。
その際にカンプ画像でダウンロードしてください。
(画像検索した際に出てくるサムネール下の画像番号の横にピクセランのマークがあるものは使用不可できません・・・)
その他の素材に関しては、フリーで提供可能なものでお願いします。

```html
<!DOCTYPE html>
<html lang="ja">
<head>
<meta charset="utf-8">
<title>hair dolvik</title>
<link href="https://fonts.googleapis.com/css2?family=Noto+Sans+JP:wght@300;400;500&family=Cormorant+Garamond:ital,wght@0,400;0,500;1,400&display=swap" rel="stylesheet">
<style>
:root{
  --white:#ffffff;
  --paper:#f0f0ee;
  --ink:#333333;
  --ink-soft:#777777;
  --line:#cfcfcc;
  --button:#3a3a3a;
  --sketch-fill:#e4e2de;
  --map:#e6e6e4;
}
*{margin:0;padding:0;box-sizing:border-box}
html,body{width:1200px;height:3752px;overflow:hidden;background:var(--white)}
body{position:relative;font-family:"Noto Sans JP",sans-serif;color:var(--ink);font-weight:300}
.abs{position:absolute}
.photo{position:absolute}
.illustration{position:absolute;background:var(--sketch-fill);border-radius:4px}
.en{font-family:"Cormorant Garamond",serif}
.brand{left:28px;top:22px;font-size:22px;font-weight:500;letter-spacing:.04em;line-height:1.2}
.nav{right:24px;top:10px;display:flex;align-items:center;gap:34px}
.nav a{color:var(--ink);text-decoration:none;font-family:"Cormorant Garamond",serif;font-size:14px}
.nav .reserve{background:var(--button);color:var(--white);padding:8px 26px;font-family:"Noto Sans JP",sans-serif;font-size:11px}
.btn{position:absolute;background:var(--button);color:var(--white);font-size:10px;letter-spacing:.2em;text-align:center;width:140px;height:24px;line-height:24px}
.btn::before{content:"→ ";}
.panel{position:absolute;background:var(--paper)}
.heading{font-family:"Cormorant Garamond",serif;font-size:22px;font-style:italic;line-height:1.2}
.body-text{font-size:11.5px;line-height:2.1;color:var(--ink)}
.small{font-size:10.5px;line-height:1.9;color:var(--ink-soft)}
.news-row{display:flex;gap:22px;font-size:10.5px;line-height:2.4;border-bottom:1px solid var(--line);white-space:nowrap}
.product-grid{position:absolute;left:0;top:2520px;width:600px;height:600px;background:var(--white)}
.product{position:absolute;width:170px;height:100px}
.product-cap{position:absolute;font-size:9.5px;line-height:1.7;width:170px}
.info-box{position:absolute;left:640px;top:3160px;width:440px;height:480px;background:var(--white);padding:34px 40px;text-align:center}
.footer{position:absolute;left:0;top:3700px;width:1200px;height:52px;border-top:1px solid var(--line);font-size:10px;display:flex;justify-content:space-between;align-items:center;padding:0 24px;color:var(--ink-soft)}
</style>
</head>
<body>

<header>
  <div class="abs brand en">hair dolvik</div>
  <nav class="abs nav">
    <a>Home</a><a>Concept</a><a>Menu</a><a>Blog</a><a>Gallery</a><a>Faq</a><a>Recruit</a>
    <span class="reserve">ご予約はこちら</span>
  </nav>
</header>

<main>
<section class="hero">
  <div class="photo" style="left:340px;top:48px;width:860px;height:352px;background:linear-gradient(90deg,#b98a62,#8e5d3a 60%,#a87a54)" role="img" aria-label="木目の外壁にサロン名のサインが掛かった写真"></div>
  <div class="illustration" style="left:110px;top:230px;width:130px;height:130px" role="img" aria-label="手描きのスタイリングチェアのイラスト"></div>
  <div class="abs body-text" style="left:60px;top:380px;width:260px;font-size:12px;line-height:1.9">自然素材とやさしい光に包まれた<br>落ち着いたプライベートサロンで<br>あなたらしいスタイルを。</div>
  <div class="abs en" style="left:60px;top:460px;width:260px;font-size:12px;font-style:italic;line-height:1.6">For our customers and our family,<br>a space where time passes gently.</div>
</section>

<section class="concept">
  <div class="photo" style="left:400px;top:400px;width:800px;height:360px;background:linear-gradient(135deg,#f4f1ec,#d8cfc4 55%,#6c4a34)" role="img" aria-label="白い壁とスタイリングチェアが並ぶ店内の写真"></div>
  <div class="abs small" style="left:272px;top:778px">Concept</div>
  <div class="abs body-text" style="left:400px;top:775px;width:760px">
    木の温もりと白を基調にした空間で、ひとりひとりに寄り添う施術を大切にしています。<br>
    お子さま連れのお客さまも安心してお過ごしいただけるよう、ゆったりとした席をご用意しました。<br>
    毎日のお手入れがしやすいスタイルを、丁寧なカウンセリングからご提案いたします。<br>
    日々の暮らしの中に、ほっとひと息つける時間をお届けします。
  </div>
  <div class="btn" style="left:560px;top:895px">MORE</div>
</section>

<section class="news-row-block">
  <div class="photo" style="left:0;top:960px;width:400px;height:520px;background:linear-gradient(160deg,#e3ddd4,#6f8a52 45%,#3f5a2e)" role="img" aria-label="白いレンガ壁と観葉植物の写真"></div>
  <div class="photo" style="left:400px;top:960px;width:400px;height:520px;background:linear-gradient(180deg,#cfc9c0,#e9e4dc 40%,#a46e48)" role="img" aria-label="木の扉と照明のある受付スペースの写真"></div>
  <div class="panel" style="left:800px;top:960px;width:400px;height:520px">
    <div class="abs heading" style="left:40px;top:60px">News</div>
    <div class="abs" style="left:40px;top:110px;width:320px">
      <div class="news-row"><span>2018.08.01</span><span>夏季休業日のお知らせを掲載しました。</span></div>
      <div class="news-row"><span>2018.07.20</span><span>新メニューのヘッドスパを始めました。</span></div>
      <div class="news-row"><span>2018.07.05</span><span>キッズスペースをリニューアルしました。</span></div>
    </div>
    <div class="btn" style="left:120px;top:330px">MORE</div>
    <div class="illustration" style="left:300px;top:400px;width:80px;height:80px" role="img" aria-label="手描きのはさみのイラスト"></div>
  </div>
</section>

<section class="menu">
  <div class="panel" style="left:0;top:1480px;width:400px;height:520px">
    <div class="illustration" style="left:40px;top:130px;width:90px;height:60px" role="img" aria-label="手描きのドライヤーのイラスト"></div>
    <div class="abs heading" style="left:40px;top:200px">Menu</div>
    <div class="abs body-text" style="left:40px;top:240px;width:320px;font-size:11px">カット・カラー・パーマなど、髪質とライフスタイルに合わせたメニューをご用意しています。</div>
    <div class="abs en small" style="left:40px;top:310px;width:320px;font-style:italic">A menu made to suit your hair and your days.</div>
    <div class="btn" style="left:40px;top:380px">MORE</div>
  </div>
  <div class="photo" style="left:400px;top:1480px;width:680px;height:520px;background:linear-gradient(180deg,#d2d6da,#b8c0c6 35%,#9d5a3c 55%,#8a4e33)" role="img" aria-label="木の大きな扉を開けたサロン入口の写真"></div>
  <div class="photo" style="left:1080px;top:1480px;width:120px;height:520px;background:linear-gradient(180deg,#ece9e4,#c0462f 40%,#ece9e4 60%)" role="img" aria-label="赤いメニューボードのある外壁の写真"></div>
</section>

<section class="staff">
  <div class="photo" style="left:0;top:2000px;width:400px;height:520px;background:linear-gradient(135deg,#e2b06c,#b77a3e 55%,#8c5a2c)" role="img" aria-label="木の床にサロン名のマットが置かれた写真"></div>
  <div class="photo" style="left:400px;top:2000px;width:400px;height:520px;background:linear-gradient(180deg,#cfcac2,#ebe7e1 45%,#8b3b2a 70%,#6a4a34)" role="img" aria-label="赤いソファと木のテーブルがある待合スペースの写真"></div>
  <div class="panel" style="left:800px;top:2000px;width:400px;height:520px">
    <div class="illustration" style="left:40px;top:120px;width:80px;height:60px" role="img" aria-label="手描きのくしのイラスト"></div>
    <div class="abs heading" style="left:40px;top:190px">Staff</div>
    <div class="abs body-text" style="left:40px;top:230px;width:320px;font-size:11px">経験豊富なスタッフが、気軽に相談できる雰囲気でお迎えいたします。</div>
    <div class="abs en small" style="left:40px;top:290px;width:320px;font-style:italic">Friendly stylists, ready to listen and help you.</div>
    <div class="btn" style="left:40px;top:360px">MORE</div>
  </div>
</section>

<section class="product-grid">
  <div class="product photo" style="left:20px;top:30px;background:linear-gradient(135deg,#d9d4cc,#55703f)" role="img" aria-label="グリーンを添えた商品の写真"></div>
  <div class="product photo" style="left:210px;top:30px;background:linear-gradient(135deg,#ede9e3,#b68a63)" role="img" aria-label="木のオブジェの写真"></div>
  <div class="product photo" style="left:400px;top:30px;background:linear-gradient(135deg,#efebe6,#c8a27c)" role="img" aria-label="ヘアケア商品の写真"></div>
  <div class="product-cap" style="left:20px;top:140px">2018.08.01<br>しっとりまとまるトリートメント入荷</div>
  <div class="product-cap" style="left:210px;top:140px">2018.07.26<br>香りの良いヘアオイルのご紹介</div>
  <div class="product-cap" style="left:400px;top:140px">2018.07.18<br>頭皮ケアのシャンプーが人気です</div>
  <div class="product photo" style="left:20px;top:270px;background:linear-gradient(135deg,#e6e1da,#a58360)" role="img" aria-label="雑貨が並ぶ棚の写真"></div>
  <div class="product photo" style="left:210px;top:270px;background:linear-gradient(135deg,#eeeae4,#8a6d52)" role="img" aria-label="小物の写真"></div>
  <div class="product photo" style="left:400px;top:270px;background:linear-gradient(135deg,#e9e6e0,#5f7d48)" role="img" aria-label="観葉植物の写真"></div>
  <div class="product-cap" style="left:20px;top:380px">2018.07.10<br>季節のカラーおすすめ色まとめ</div>
  <div class="product-cap" style="left:210px;top:380px">2018.07.02<br>ご自宅でできるスタイリング</div>
  <div class="product-cap" style="left:400px;top:380px">2018.06.25<br>夏の紫外線から髪を守る方法</div>
  <div class="btn" style="left:230px;top:520px">MORE</div>
</section>
<div class="photo" style="left:600px;top:2520px;width:600px;height:600px;background:linear-gradient(180deg,#1f3f9e,#2c4fb0 30%,#7a4a2e 55%,#5a3a26)" role="img" aria-label="夜に照明が灯るサロン外観の写真"></div>

<section class="access">
  <div class="photo" style="left:0;top:3120px;width:1200px;height:580px;background:var(--map)" role="img" aria-label="サロン周辺の地図"></div>
  <div class="info-box">
    <div class="heading" style="font-size:18px">Access</div>
    <div class="small" style="margin-top:8px">最寄り駅から徒歩5分、駐車場も2台ご用意しています。</div>
    <div class="heading" style="font-size:18px;margin-top:26px">Open</div>
    <div class="small">10:00 - 19:00</div>
    <div class="heading" style="font-size:18px;margin-top:26px">Holiday</div>
    <div class="small">毎週火曜日・第三月曜日</div>
    <div class="heading" style="font-size:18px;margin-top:26px">Contact</div>
    <div class="small">〒000-0000 緑が丘町1丁目2-3<br>TEL 000-000-0000<br>ご予約は下記ボタンよりお願いします</div>
  </div>
</section>
</main>

<footer class="footer">
  <span>Privacy Policy</span>
  <span>Copyright © hair dolvik</span>
</footer>

</body>
</html>
```